Saffron Ember

we need a flyer design. for an A4 sheet folded into 3 layers/pages.
for an Indian fast food take away. Please use up to date UK standard menu design.
Any more info needed can contact us anytime by email.
word document of item for the flyer attached.

Target Market(s)

Indian Food lovers

Industry/Entity Type

Indian Restaurant

Font styles to use
Decorative
Script

Colors
cbe087
abd036
fbf289
f37022

Requirements
Must have
• Can you please bleed the menu so that I can show it to the printer guy
Nice to have
• modern menu

```html
<!DOCTYPE html>
<html lang="en">
<head>
<meta charset="utf-8">
<title>Saffron Ember – Delivery Menu</title>
<link rel="stylesheet" href="https://fonts.googleapis.com/css2?family=Amatic+SC:wght@700&family=Lobster&family=Open+Sans:wght@400;600;700&family=Permanent+Marker&display=swap">
<style>
  :root{
    --backdrop:#9a9a9a;
    --paper:#ffffff;
    --orange:#f37022;
    --red:#d9302a;
    --deep-red:#b8221f;
    --yellow:#fbf289;
    --gold:#f7e43c;
    --ink:#333333;
    --muted:#777777;
  }
  *{box-sizing:border-box;margin:0;padding:0}
  html,body{width:1200px;height:600px;overflow:hidden}
  body{background:var(--backdrop);font-family:"Open Sans",Arial,sans-serif;position:relative}
  .flyer{position:absolute;left:180px;top:20px;width:840px;height:560px;background:var(--orange);box-shadow:0 4px 18px rgba(0,0,0,.25)}
  .panel{position:absolute;top:0;width:280px;height:560px}
  .panel--inner{left:0;background:var(--paper);padding:26px 26px 0 30px;color:var(--ink)}
  .panel--pizza{left:280px}
  .panel--cover{left:560px}
  .script-heading{font-family:"Lobster",cursive;font-weight:400}
  .panel--inner .script-heading{color:var(--orange);font-size:24px;text-align:center;margin-bottom:6px}
  .meal-title{color:var(--orange);font-weight:700;font-size:10.5px;margin-top:6px}
  .meal-list{list-style:none;font-size:10.5px;line-height:1.45;margin:2px 0 10px}
  .meal-list li::before{content:"• "}
  .drinks{margin-top:18px}
  .drink-row{display:flex;font-size:10.5px;line-height:1.6}
  .drink-row .leader{flex:1;border-bottom:1px dashed var(--ink);margin:0 4px 5px}
  .drink-row .price{color:var(--orange);font-weight:700}
  .fine-print{margin-top:12px;font-size:8px;line-height:1.5;color:var(--muted)}
  .photo{position:absolute;left:430px;top:0;width:410px;height:210px}
  .pizza-menu{position:absolute;left:22px;top:140px;width:240px;color:var(--paper)}
  .pizza-menu .script-heading{font-size:26px}
  .size-head{text-align:right;color:var(--gold);font-weight:700;font-size:11px;margin-top:-6px}
  .pizza-item{margin-top:6px}
  .pizza-row{display:flex;font-size:11.5px;font-weight:600}
  .pizza-row .leader{flex:1;border-bottom:1px dashed var(--paper);margin:0 4px 5px}
  .pizza-row .price{color:var(--gold);font-weight:700}
  .pizza-desc{font-size:8px;opacity:.9}
  .red-band{position:absolute;left:280px;top:385px;width:560px;height:175px}
  .back-brand{position:absolute;left:280px;top:470px;width:280px;text-align:center;color:var(--paper)}
  .back-brand .name{font-family:"Permanent Marker",cursive;font-size:22px;letter-spacing:1px}
  .back-brand .phone{font-size:11px}
  .cover-title{position:absolute;left:22px;top:212px;width:250px;color:var(--paper);font-family:"Permanent Marker",cursive;font-size:40px;line-height:1}
  .cover-tagline{position:absolute;left:24px;top:300px;color:var(--gold);font-family:"Amatic SC",cursive;font-size:26px;letter-spacing:1px}
  .delivery{position:absolute;left:0;top:340px;width:280px;text-align:center;font-family:"Amatic SC",cursive}
  .delivery .title{color:var(--deep-red);font-size:40px;line-height:1}
  .delivery .areas{color:var(--gold);font-size:22px;line-height:1.05;margin-top:4px}
  .contact{position:absolute;left:0;top:470px;width:280px;text-align:center;color:var(--paper);font-size:12px;line-height:1.5}
</style>
</head>
<body>
<main class="flyer">
  <section class="panel panel--inner">
    <h2 class="script-heading">Meals</h2>
    <p class="meal-title">Set Meal A for 1<br>Non-vegetarian £10.00</p>
    <ul class="meal-list">
      <li>Chicken tikka starter</li><li>Chicken tikka masala</li><li>Pilau Rice</li><li>Plain Naan</li><li>Poppadoms and spiced onions</li><li>Choice of soft drink</li>
    </ul>
    <p class="meal-title">Set Meal for 2 £25.00</p>
    <ul class="meal-list">
      <li>Onion bhaji</li><li>Chicken tikka starter</li><li>Chicken tikka masala</li><li>Lamb Rogan Josh</li><li>2 x Pilau rice</li><li>Plain naan</li><li>Poppadum with spiced onion</li><li>2 soft drinks</li>
    </ul>
    <div class="drinks">
      <h2 class="script-heading">Soft Drinks</h2>
      <div class="drink-row"><span>Lemon Soda 330ml can</span><span class="leader"></span><span class="price">£1.00</span></div>
      <div class="drink-row"><span>Orange Soda 330ml can</span><span class="leader"></span><span class="price">£1.00</span></div>
      <div class="drink-row"><span>Cola 330ml can</span><span class="leader"></span><span class="price">£1.00</span></div>
      <div class="drink-row"><span>Diet Cola 330ml can</span><span class="leader"></span><span class="price">£1.00</span></div>
    </div>
    <p class="fine-print">All our dishes are freshly cooked to order. Please tell staff about any allergies before ordering. Prices may change without notice. Minimum order for delivery £10.</p>
  </section>

  <section class="panel panel--pizza">
    <div class="pizza-menu">
      <h2 class="script-heading">Pizza</h2>
      <p class="size-head">10" / 12"</p>
      <div class="pizza-item"><div class="pizza-row"><span>1. Margherita</span><span class="leader"></span><span class="price">£4.50/£5.00</span></div><p class="pizza-desc">Tomato sauce and mozzarella</p></div>
      <div class="pizza-item"><div class="pizza-row"><span>2. Mexican</span><span class="leader"></span><span class="price">£6.00/£7.00</span></div><p class="pizza-desc">Spicy beef, peppers, onions, jalapeños</p></div>
      <div class="pizza-item"><div class="pizza-row"><span>3. Hawaiian</span><span class="leader"></span><span class="price">£5.00/£6.00</span></div><p class="pizza-desc">Ham and pineapple</p></div>
      <div class="pizza-item"><div class="pizza-row"><span>4. Milano</span><span class="leader"></span><span class="price">£6.00/£7.00</span></div><p class="pizza-desc">Pepperoni, mushrooms, olives</p></div>
      <div class="pizza-item"><div class="pizza-row"><span>5. Vegetarian</span><span class="leader"></span><span class="price">£5.00/£6.00</span></div><p class="pizza-desc">Peppers, onions, sweetcorn, tomato</p></div>
      <div class="pizza-item"><div class="pizza-row"><span>6. Garlic Bread</span><span class="leader"></span><span class="price">£3.50/£4.50</span></div></div>
    </div>
  </section>

  <svg class="photo" viewBox="0 0 410 210" role="img" aria-label="Photograph of freshly baked pizzas topped with basil, artichoke and ham">
    <defs>
      <linearGradient id="pizzaTone" x1="0" y1="0" x2="1" y2="1">
        <stop offset="0" stop-color="#e4b98a"/>
        <stop offset=".45" stop-color="#c8553a"/>
        <stop offset=".8" stop-color="#9e3a24"/>
        <stop offset="1" stop-color="#6f8a3a"/>
      </linearGradient>
    </defs>
    <path d="M0 0 H410 V205 L380 200 L350 208 L300 198 L240 206 L190 196 L150 190 L140 150 L110 132 L60 126 L20 132 L0 128 Z" fill="url(#pizzaTone)"/>
  </svg>

  <svg class="red-band" viewBox="0 0 560 175" preserveAspectRatio="none" aria-hidden="true">
    <path d="M0 12 L18 4 L34 14 L52 6 L70 16 L92 8 L110 18 L132 10 L150 22 L172 12 L196 20 L220 10 L244 18 L270 26 L290 30 L312 24 L336 34 L360 28 L384 40 L410 36 L436 46 L462 42 L490 52 L516 48 L540 56 L560 52 V175 H0 Z" fill="var(--red)"/>
  </svg>

  <div class="back-brand">
    <p class="name">SAFFRON EMBER</p>
    <p class="phone">Phone Number</p>
  </div>

  <section class="panel panel--cover">
    <h1 class="cover-title">SAFFRON EMBER</h1>
    <p class="cover-tagline">KEBAB, PIZZA, CURRY</p>
    <div class="delivery">
      <p class="title">Delivery Menu</p>
      <p class="areas">WE DELIVER TO:<br>HOLLYBROOK, KILMORY, DUNBEG</p>
    </div>
    <address class="contact" style="font-style:normal">
      14 Mill Lane, Ardvale<br>Opening hours 5pm - 10.30pm<br>Phone number
    </address>
  </section>
</main>
</body>
</html>
```